flyer design for landscape group. i have enclosed my business card with logo

we are a local domestic and commercial landscaping group based in wokingham berkshire .we offer competitive landscaping solutions with a broad knowledge helping us solve problems in many fields such as new lawns, lawn care,tree care ,tree removal,hard and soft landscaping, decking, fencing ,garden or land clearance or just helping you with general maintanence. Being fully insured and certified for the job ,our excellent attention to detail has seen us recognised by local authorities and work for them on maintenance programmes performing in a safe and efficient manner

Target Market(s)

high end gardens commercial property

Industry/Entity Type

Landscaping

Requirements
Must have
• my logo . and some minimal sleek black and white design with small injections of colour
Should not have
• please do not include my full name or address only email and telephone

```html
<!DOCTYPE html>
<html lang="en">
<head>
<meta charset="utf-8">
<title>Fernbrook – Landscaping Solutions Flyer</title>
<link rel="stylesheet" href="https://fonts.googleapis.com/css2?family=Nunito+Sans:wght@300;400;700&family=Roboto+Mono:ital,wght@1,700&display=swap">
<style>
  :root {
    --forest: #1e6a3a;
    --leaf: #a9d46c;
    --cream: #f6ebdc;
    --bark: #4b2f22;
    --amber: #f29a1f;
    --contact-green: #2a7b3a;
    --white: #ffffff;
    --text-light: #f3f7f1;
    --lawn: #4f9a34;
    --lawn-deep: #3f7f2a;
    --foliage: #3e5e2c;
    --brick: #a8654f;
  }
  * { box-sizing: border-box; margin: 0; padding: 0; }
  html, body { width: 1200px; height: 851px; overflow: hidden; background: var(--white); }
  .flyer {
    position: relative;
    width: 1200px;
    height: 851px;
    overflow: hidden;
    font-family: "Nunito Sans", Arial, sans-serif;
    background: var(--white);
  }
  .hero-photo {
    position: absolute;
    left: 0; top: 0;
    width: 1200px; height: 452px;
    background:
      radial-gradient(ellipse 420px 200px at 780px 110px, rgba(168,101,79,0.85), rgba(168,101,79,0) 100%),
      radial-gradient(ellipse 360px 260px at 200px 120px, rgba(62,94,44,0.9), rgba(62,94,44,0) 100%),
      radial-gradient(ellipse 260px 220px at 1100px 230px, rgba(47,92,60,0.8), rgba(47,92,60,0) 100%),
      linear-gradient(180deg, #5f7d4c 0%, #58803f 45%, var(--lawn) 65%, var(--lawn-deep) 100%);
  }
  .courtyard-photo {
    position: absolute;
    left: 0; top: 452px;
    width: 329px; height: 270px;
    background: linear-gradient(170deg, #6e6e6e 0%, #8c8c8c 40%, #555555 70%, #a9a9a9 100%);
  }
  .brand-panel {
    position: absolute;
    left: 329px; top: 452px;
    width: 322px; height: 270px;
    background: var(--cream);
  }
  .brand-mark {
    position: absolute;
    left: 137px; top: 68px;
    width: 48px; height: 48px;
    border-radius: 50%;
    background: var(--amber);
  }
  .brand-name {
    position: absolute;
    left: 0; right: 0; top: 150px;
    text-align: center;
    font-weight: 300;
    font-size: 36px;
    line-height: 44px;
    letter-spacing: 2px;
    color: var(--bark);
  }
  .contact {
    position: absolute;
    left: 40px; top: 742px;
    font-family: "Roboto Mono", "Courier New", monospace;
    font-style: italic;
    font-weight: 700;
    font-size: 25px;
    line-height: 29px;
    color: var(--contact-green);
    letter-spacing: -0.5px;
  }
  .contact .label { color: var(--amber); }
  .services-panel {
    position: absolute;
    left: 651px; top: 342px;
    width: 549px; height: 509px;
    background: var(--forest);
    color: var(--text-light);
  }
  .tagline {
    font-family: "Roboto Mono", "Courier New", monospace;
    font-style: italic;
    font-weight: 700;
    font-size: 16px;
    line-height: 20px;
    color: var(--text-light);
    display: flex;
    align-items: center;
    gap: 8px;
  }
  .tagline-top {
    position: absolute;
    left: 44px; top: 18px;
  }
  .tagline-top .rule {
    display: block;
    width: 58px; height: 1px;
    background: var(--text-light);
  }
  .tagline-bottom {
    position: absolute;
    left: 0; right: 0; top: 448px;
    justify-content: center;
    color: var(--leaf);
  }
  .services-title {
    position: absolute;
    left: 45px; top: 70px;
    font-weight: 300;
    font-size: 36px;
    line-height: 44px;
    letter-spacing: 0.3px;
    color: var(--white);
  }
  .service-list {
    position: absolute;
    left: 47px; top: 139px;
    width: 450px;
    list-style: none;
  }
  .service { margin-bottom: 25px; }
  .service-name {
    font-weight: 700;
    font-size: 20px;
    line-height: 28px;
    color: var(--leaf);
  }
  .service-detail {
    font-weight: 400;
    font-size: 21px;
    line-height: 30px;
    color: var(--text-light);
  }
</style>
</head>
<body>
<main class="flyer">
  <div class="hero-photo" role="img" aria-label="Photograph of a manicured lawn in front of a red-brick house with stone gate pillars, shrubs and flowering borders"></div>

  <div class="courtyard-photo" role="img" aria-label="Black and white photograph of a modern courtyard garden with small trees and paving"></div>

  <div class="brand-panel">
    <span class="brand-mark"></span>
    <span class="brand-name">FERNBROOK</span>
  </div>

  <address class="contact">
    <div><span class="label">m:</span> 07700 900 482</div>
    <div><span class="label">e:</span> tom@fernbrookgardens.co.uk</div>
    <div><span class="label">w:</span> www.fernbrookgardens.co.uk</div>
  </address>

  <section class="services-panel">
    <p class="tagline tagline-top"><span class="rule"></span>Domestic and Commercial Landscaping<span class="rule"></span></p>
    <h1 class="services-title">LANDSCAPING SOLUTIONS</h1>
    <ul class="service-list">
      <li class="service">
        <h2 class="service-name">Lawns</h2>
        <p class="service-detail">New lawns, lawn care</p>
      </li>
      <li class="service">
        <h2 class="service-name">Trees</h2>
        <p class="service-detail">Tree care ,tree removal</p>
      </li>
      <li class="service">
        <h2 class="service-name">Landscaping</h2>
        <p class="service-detail">Hard and soft landscaping, decking, fencing, garden or land clearance or just helping you with general maintanence</p>
      </li>
    </ul>
    <p class="tagline tagline-bottom">Domestic and Commercial Landscaping</p>
  </section>
</main>
</body>
</html>
```